North American Image Consultant needs a process design and a method design

I am an Image/style consultant who works with business professionals in the Toronto area. My product name is called " S.H.A.R.E." I help people understand how your " Style, Habits, Attitude, Reach and Energy. I help people create a professional appearance in a business casual/digital world, from head to toe. I work with them through all 4 seasons, to achieve consistency and confidence to help them look and feel amazing, inside and out.. easily and effortlessly. My main colour is aqua blue, I don't want any neon or primary colours. I would like it to appeal to both men and women ( but mostly women)
The final design should be an easy to follow path to success with an understanding of what S.H.A.R.E will do for them.

Target Market(s)

mid level executive business professionals 38-58 yrs old they want to look and feel amazing inside and out. They want to up their game, get the promotion, nail the interview , and feel they're relevant and taken seriously in a leadership way.

Font styles to use
Serif

Colors
b7a5cd
886aae
85cae6
33a6d7
33b8a4
f04a50
00a990
e34297
85acd3

Requirements
Must have
• A classy, casual feel. A positive feel good feeling
Nice to have
• A 3 colour balance ( Not black based)
Should not have
• Too many squares
too many squiggly lines.
Not too masculine/feminine
too childish/youthful
Not office focused or bank focused

```html
<!DOCTYPE html>
<html lang="en">
<head>
<meta charset="utf-8">
<title>S.H.A.R.E. – Maintaining a professional appearance</title>
<link rel="stylesheet" href="https://fonts.googleapis.com/css2?family=Gelasio:wght@400;700&display=swap">
<style>
  :root {
    --ink: #0d0d0d;
    --muted: #8a8a8a;
    --rule: #a6a6a6;
    --lavender: #b7a5cd;
    --plum: #886aae;
    --sky: #85cae6;
    --ocean: #33a6d7;
    --aqua: #33b8a4;
    --hub: #e0e0e0;
    --paper: #ffffff;
  }
  * { margin: 0; padding: 0; box-sizing: border-box; }
  html, body { width: 1200px; height: 675px; overflow: hidden; background: var(--paper); }
  body { font-family: "Gelasio", Georgia, serif; color: var(--ink); }
  .canvas { position: relative; width: 1200px; height: 675px; }

  .header { position: absolute; left: 96px; top: 50px; width: 1020px; height: 34px; border-bottom: 3px solid var(--rule); }
  .header__title { position: absolute; left: 0; bottom: 6px; font-size: 24px; font-weight: 700; letter-spacing: 0.5px; }
  .header__tagline { position: absolute; right: 0; bottom: 6px; font-size: 20px; color: var(--muted); }

  .wheel { position: absolute; left: 0; top: 0; }
  .wheel__hub-text { font-family: "Gelasio", Georgia, serif; font-weight: 700; font-size: 31px; fill: var(--ink); }
  .icon { fill: none; stroke: var(--paper); stroke-width: 2; stroke-linecap: round; stroke-linejoin: round; }

  .pillar { position: absolute; }
  .pillar__name { font-size: 22px; font-weight: 700; line-height: 26px; white-space: nowrap; }
  .pillar__note { font-size: 15px; line-height: 22px; white-space: nowrap; }
  .pillar--style    { left: 820px; top: 136px; }
  .pillar--habits   { left: 880px; top: 384px; }
  .pillar--attitude { left: 479px; top: 605px; }
  .pillar--reach    { left: 158px; top: 384px; }
  .pillar--energy   { left: 250px; top: 137px; }
</style>
</head>
<body>
<main class="canvas">
  <header class="header">
    <h1 class="header__title">S.H.A.R.E.</h1>
    <p class="header__tagline">Maintaining a professional appearance in a business casual world</p>
  </header>

  <svg class="wheel" width="1200" height="675" viewBox="0 0 1200 675" aria-label="S.H.A.R.E. five-part wheel">
    <g stroke="#fff" stroke-width="3" stroke-linejoin="round">
      <path fill="var(--aqua)" d="M607 112 A237 237 0 0 1 832.4 275.8 L721.1 311.9 A120 120 0 0 0 607 229 Z"/>
      <path fill="var(--sky)" d="M832.4 275.8 A237 237 0 0 1 746.3 540.7 L677.5 446.1 A120 120 0 0 0 721.1 311.9 Z"/>
      <path fill="var(--ocean)" d="M746.3 540.7 A237 237 0 0 1 467.7 540.7 L536.5 446.1 A120 120 0 0 0 677.5 446.1 Z"/>
      <path fill="var(--plum)" d="M467.7 540.7 A237 237 0 0 1 381.6 275.8 L492.9 311.9 A120 120 0 0 0 536.5 446.1 Z"/>
      <path fill="var(--lavender)" d="M381.6 275.8 A237 237 0 0 1 607 112 L607 229 A120 120 0 0 0 492.9 311.9 Z"/>

      <circle cx="628" cy="180" r="20" fill="var(--lavender)"/>
      <circle cx="775" cy="317" r="20" fill="var(--aqua)"/>
      <circle cx="689" cy="500" r="20" fill="var(--sky)"/>
      <circle cx="488" cy="478" r="20" fill="var(--ocean)"/>
      <circle cx="450" cy="277" r="20" fill="var(--plum)"/>

      <circle cx="682" cy="245" r="21" fill="var(--hub)"/>
      <circle cx="729" cy="389" r="21" fill="var(--hub)"/>
      <circle cx="607" cy="477" r="21" fill="var(--hub)"/>
      <circle cx="485" cy="389" r="21" fill="var(--hub)"/>
      <circle cx="532" cy="245" r="21" fill="var(--hub)"/>
      <circle cx="607" cy="349" r="113" fill="var(--hub)"/>
    </g>
    <circle cx="607" cy="349" r="110" fill="var(--hub)"/>
    <circle cx="607" cy="349" r="84" fill="var(--paper)"/>
    <text class="wheel__hub-text" x="609" y="360" text-anchor="middle">S.H.A.R.E.</text>

    <!-- stopwatch -->
    <g class="icon">
      <circle cx="490" cy="200" r="21"/>
      <circle cx="490" cy="200" r="16"/>
      <path d="M484 173h12M490 173v6M507 181l4 4M490 200l6 -8M490 188v2M502 200h-2M490 212v-2M478 200h2"/>
    </g>
    <!-- org chart -->
    <g class="icon">
      <rect x="713" y="168" width="18" height="12" rx="2"/>
      <path d="M722 180v8M702 188h40M702 188v6M722 188v6M742 188v6"/>
      <rect x="695" y="194" width="14" height="10" rx="2"/>
      <rect x="715" y="194" width="14" height="10" rx="2"/>
      <rect x="735" y="194" width="14" height="10" rx="2"/>
    </g>
    <!-- network -->
    <g class="icon">
      <circle cx="794" cy="382" r="10"/>
      <circle cx="777" cy="407" r="8"/>
      <circle cx="808" cy="411" r="10"/>
      <path d="M788 390l-6 10M800 391l4 10M786 408h12M770 373v-3M784 380l-14 -8M818 380h10M817 389h10"/>
      <circle cx="770" cy="370" r="2"/>
      <circle cx="829" cy="380" r="2"/>
      <circle cx="829" cy="389" r="2"/>
    </g>
    <!-- megaphone -->
    <g class="icon">
      <path d="M590 545l18 -28l16 22l-26 12z"/>
      <path d="M590 545l-9 4l5 9l10 -4"/>
      <path d="M593 552l6 10l5 -3l-5 -9"/>
      <path d="M613 518a9 9 0 0 1 7 -6M618 522a14 14 0 0 1 9 -8"/>
    </g>
    <!-- trophy -->
    <g class="icon">
      <path d="M405 367h32v14a16 16 0 0 1 -32 0z"/>
      <path d="M405 371h-6v6a10 10 0 0 0 8 9M437 371h6v6a10 10 0 0 1 -8 9"/>
      <circle cx="421" cy="380" r="7"/>
      <path d="M421 397v9M412 414h18M414 414l3 -8h8l3 8"/>
    </g>
  </svg>

  <section class="pillar pillar--style">
    <h2 class="pillar__name">S - Style</h2>
    <p class="pillar__note">Level of authority</p>
  </section>
  <section class="pillar pillar--habits">
    <h2 class="pillar__name">H - Habits</h2>
    <p class="pillar__note">Influence of environment</p>
  </section>
  <section class="pillar pillar--attitude">
    <h2 class="pillar__name">A - Attitude</h2>
    <p class="pillar__note">The ‘Sound’ of your presence when you walk into a room</p>
  </section>
  <section class="pillar pillar--reach">
    <h2 class="pillar__name">R - Reach</h2>
    <p class="pillar__note">Achieve consistent results</p>
  </section>
  <section class="pillar pillar--energy">
    <h2 class="pillar__name">E - Energy</h2>
    <p class="pillar__note">Save more, spend less</p>
  </section>
</main>
</body>
</html>
```